Need a simple buisness card for my plumbing business. Would like it to be black background with white text.

Industry/Entity Type

Business

Requirements
Must have
• On the front of the card I need to have,
TKB PLUMBING SERVICES
PLUMBERS, DRAINERS & GASFITTERS
Dorian Wellsby
0471596083
Info@tkbplumbingservices.com.au
LIC No 517483f
ABN No 61907354218
On the back I need in point form
Domestic,industrial,commercial, all new installations, renovations, sewer renewals, repairs,
Fully licensed and insured
Nice to have
• A nice simple logo

```html
<!DOCTYPE html>
<html lang="en">
<head>
<meta charset="utf-8">
<title>TKB Plumbing Services – Business Card</title>
<link href="https://fonts.googleapis.com/css2?family=Arimo:wght@400;700&display=swap" rel="stylesheet">
<style>
  :root {
    --backdrop: #d6d6d6;
    --card: #000000;
    --ink-light: #ffffff;
    --ink-dark: #000000;
    --panel: #ffffff;
  }
  * { margin: 0; padding: 0; box-sizing: border-box; }
  html, body {
    width: 1200px; height: 900px; overflow: hidden;
    background: var(--backdrop);
    font-family: "Arimo", Arial, sans-serif;
  }
  .stage { position: relative; width: 1200px; height: 900px; }

  .card {
    position: absolute;
    width: 499px; height: 311px;
    background: var(--card);
    border-radius: 14px;
    color: var(--ink-light);
    overflow: hidden;
    box-shadow: 2px 3px 6px rgba(0,0,0,0.25);
  }
  .card--back  { left: 544px; top: 127px; }
  .card--front { left: 162px; top: 470px; }

  .brand-mark {
    position: absolute;
    font-weight: 700;
    font-size: 48px;
    letter-spacing: 1px;
    line-height: 1;
    color: var(--ink-light);
  }
  .brand-name {
    position: absolute;
    font-size: 17px;
    font-weight: 400;
    white-space: nowrap;
    color: var(--ink-light);
  }

  /* back */
  .card--back .brand-mark { left: 99px; top: 106px; }
  .card--back .brand-name { left: 36px; top: 168px; }
  .services-panel {
    position: absolute;
    left: 284px; top: 49px;
    width: 215px; height: 185px;
    background: var(--panel);
    color: var(--ink-dark);
    padding: 14px 0 0 16px;
    font-size: 14.5px;
  }
  .services-list { list-style: none; line-height: 18px; }
  .services-list li::before { content: "• "; }
  .services-note { margin-top: 14px; }

  /* front */
  .card--front .brand-mark { left: 302px; top: 40px; }
  .card--front .brand-name { left: 232px; top: 110px; }
  .name-band {
    position: absolute;
    left: 0; top: 96px;
    width: 190px; height: 44px;
    background: var(--panel);
    color: var(--ink-dark);
    font-weight: 700;
    font-size: 18px;
    line-height: 44px;
    padding-left: 31px;
    white-space: nowrap;
  }
  .name-rule {
    position: absolute;
    left: 193px; top: 90px;
    width: 7px; height: 56px;
    background: var(--panel);
    border-radius: 3px;
  }
  .contact {
    position: absolute;
    left: 234px; top: 186px;
    font-size: 14px;
    line-height: 19px;
  }
  .trades {
    position: absolute;
    left: 234px; top: 261px;
    font-size: 14.5px;
    white-space: nowrap;
  }
  .registration {
    position: absolute;
    left: 31px; top: 243px;
    font-size: 13px;
    line-height: 20px;
  }
</style>
</head>
<body>
<main class="stage">

  <section class="card card--back" aria-label="Card back">
    <div class="brand-mark">TKB</div>
    <div class="brand-name">TKB PLUMBING SERVICES</div>
    <div class="services-panel">
      <ul class="services-list">
        <li>Domestic</li>
        <li>Industrial</li>
        <li>Commercial</li>
        <li>All new installations</li>
        <li>Renovations</li>
        <li>Sewer renewals</li>
        <li>Repairs</li>
      </ul>
      <p class="services-note">Fully Licensed &amp; Insured</p>
    </div>
  </section>

  <section class="card card--front" aria-label="Card front">
    <div class="name-band">Dorian Wellsby</div>
    <div class="name-rule"></div>
    <div class="brand-mark">TKB</div>
    <div class="brand-name">TKB PLUMBING SERVICES</div>
    <div class="contact">
      <p>0471596083</p>
      <p>Info@tkbplumbingservices.com.au</p>
      <p>www.tkbplumbingservices.com.au</p>
    </div>
    <p class="trades">Plumbers • Drainers • Gasfitters</p>
    <div class="registration">
      <p>LIC No 517483f</p>
      <p>ABN No 61907354218</p>
    </div>
  </section>

</main>
</body>
</html>
```